Election campaign for community-managed mental health sector - Webpage Banner and Logo

Please refer to the attached design brief for all the information and details. This is a campaign logo, and graphic design for the webpage banner.

Target Market(s)

Primary • NSW Ministers, Shadow Ministers, MPs and political advisers • Treasury and health policy decision-makers • Other key decision makers and stakeholders Secondary • Community-managed mental health workers • Sector leaders and advocates • People with lived experience and their families

Industry/Entity Type

Community-managed mental health sector in NSW, Australia

Other font styles liked:
• Gotham Family

Requirements
Must have
• Please refer to design brief
Nice to have
Should not have
• Completely AI generated - see design brief for more information.

```html
<!DOCTYPE html>
<html lang="en">
<head>
<meta charset="utf-8">
<title>Care Beyond Crisis — Campaign Banner</title>
<link href="https://fonts.googleapis.com/css2?family=Bebas+Neue&family=IBM+Plex+Mono:wght@400;500;600&display=swap" rel="stylesheet">
<style>
  :root {
    --paper: #f7f4f0;
    --violet: #4a2f7e;
    --amber: #f0901e;
    --white: #ffffff;
  }
  html, body {
    margin: 0;
    padding: 0;
    width: 1200px;
    height: 900px;
    overflow: hidden;
    background: var(--paper);
  }
  .banner {
    position: relative;
    width: 1200px;
    height: 900px;
    overflow: hidden;
    background: var(--paper);
    font-family: "IBM Plex Mono", monospace;
    color: var(--violet);
  }
  .wordmark {
    position: absolute;
    left: 0;
    top: 0;
    width: 1200px;
    height: 900px;
  }
  .wordmark__text {
    font-family: "Bebas Neue", "Oswald", sans-serif;
    fill: var(--violet);
  }
  .connector {
    position: absolute;
    left: 0;
    top: 0;
    width: 1200px;
    height: 900px;
    pointer-events: none;
  }
  .subhead {
    position: absolute;
    left: 868px;
    top: 296px;
    margin: 0;
    font-family: "IBM Plex Mono", monospace;
    font-weight: 500;
    font-size: 30px;
    line-height: 32px;
    color: var(--amber);
    letter-spacing: 0.5px;
  }
  .tagline {
    position: absolute;
    left: 792px;
    top: 632px;
    width: 382px;
    margin: 0;
    font-size: 9.5px;
    line-height: 12px;
    font-weight: 600;
    letter-spacing: 1.2px;
    white-space: nowrap;
  }
  .photo-slot {
    position: absolute;
    left: 1033px;
    top: 696px;
    width: 138px;
    height: 93px;
    border: 2px solid var(--amber);
    background: radial-gradient(ellipse at 55% 45%, #a89a90 0%, #6e625c 40%, #2e2a28 80%, #1b1a19 100%);
  }
  .footer-meta {
    position: absolute;
    left: 24px;
    top: 852px;
    margin: 0;
    font-size: 12px;
    font-weight: 500;
    letter-spacing: 0.6px;
  }
  .action-bar {
    position: absolute;
    left: 655px;
    top: 842px;
    width: 520px;
    height: 33px;
    display: flex;
  }
  .action-bar__label {
    width: 147px;
    background: var(--violet);
    color: var(--white);
    display: flex;
    align-items: center;
    justify-content: center;
    font-size: 14px;
    letter-spacing: 1px;
  }
  .action-bar__fill {
    width: 188px;
    margin-left: 1px;
    background: var(--violet);
  }
  .action-bar__cta {
    flex: 1;
    border: 1.5px solid var(--violet);
    background: var(--white);
    color: var(--violet);
    display: flex;
    align-items: center;
    justify-content: center;
    font-size: 14px;
    letter-spacing: 1px;
    text-decoration: none;
  }
</style>
</head>
<body>
  <main class="banner">
    <svg class="wordmark" viewBox="0 0 1200 900" aria-label="Care">
      <text class="wordmark__text" x="24" y="643" font-size="885" textLength="754" lengthAdjust="spacingAndGlyphs">CARE</text>
    </svg>

    <svg class="connector" viewBox="0 0 1200 900" aria-hidden="true">
      <line x1="571" y1="331" x2="845" y2="331" stroke="var(--amber)" stroke-width="2"/>
      <path d="M718 651 C726 720 770 744 815 744 L1033 744" fill="none" stroke="var(--amber)" stroke-width="1.6" stroke-dasharray="9 7"/>
    </svg>

    <h2 class="subhead">BEYOND<br>CRISIS</h2>

    <p class="tagline">A PUBLIC POLICY CAMPAIGN FOR SUSTAINED COMMUNITY SUPPORT</p>

    <div class="photo-slot" role="img" aria-label="Photograph of two pairs of hands clasped together in support"></div>

    <p class="footer-meta">CMHN • 2025–2027</p>

    <nav class="action-bar">
      <span class="action-bar__label">REPORT 01</span>
      <span class="action-bar__fill"></span>
      <a class="action-bar__cta" href="#brief">READ THE BRIEF</a>
    </nav>
  </main>
</body>
</html>
```